New Web Design Project

See attachments on the content and concept. Very important that the flow of the tiers stand out

Target Market(s)

Food and Beverage Manufacturing

Industry/Entity Type

Food and Beverage

Coding

Coded - Design and coding required

Number of Pages Required

3 page

Colors
0054AA
0677BA
7BADD7
CADEEF
E8F1F8

```html
<!DOCTYPE html>
<html lang="en">
<head>
<meta charset="utf-8">
<title>Crestline Consulting Group — SQF Consulting</title>
<link href="https://fonts.googleapis.com/css2?family=Libre+Baskerville:wght@400;700&family=Poppins:wght@400;500;600;700&display=swap" rel="stylesheet">
<style>
:root{
  --blue:#0054AA;
  --blue-mid:#0677BA;
  --blue-soft:#7BADD7;
  --blue-pale:#CADEEF;
  --blue-mist:#E8F1F8;
  --navy:#0B3F86;
  --ink:#1B2430;
  --muted:#5B6675;
  --white:#ffffff;
}
*{box-sizing:border-box;margin:0;padding:0}
html,body{width:1200px;height:4605px;overflow:hidden}
body{font-family:"Poppins",sans-serif;color:var(--ink);background:var(--white);position:relative}
.serif{font-family:"Libre Baskerville",serif;font-weight:400}
section,header,footer{position:absolute;left:0;width:1200px}
.abs{position:absolute}

/* nav */
.nav{top:0;height:75px;background:var(--white);box-shadow:0 1px 6px rgba(0,0,0,.06);z-index:3}
.brand{position:absolute;left:93px;top:10px;display:flex;align-items:center;gap:10px}
.brand-dot{width:46px;height:46px;border-radius:50%;border:3px solid var(--blue);flex:none}
.brand-name{font-weight:700;font-size:17px;color:var(--blue);line-height:1.1}
.brand-tag{font-size:11px;color:var(--blue-mid);margin-top:2px}
.nav-links{position:absolute;left:448px;top:28px;display:flex;gap:44px;font-size:12px;font-weight:500;letter-spacing:.5px;color:var(--ink)}
.nav-cta{position:absolute;right:73px;top:16px;height:44px;width:222px;border-radius:22px;background:var(--navy);color:#fff;font-size:11.5px;font-weight:600;display:flex;align-items:center;padding-left:26px;gap:12px}
.arrow-dot{width:26px;height:26px;border-radius:50%;background:#fff;display:flex;align-items:center;justify-content:center}

/* hero */
.hero{top:75px;height:617px;background:linear-gradient(120deg,#0B3F86 0%,var(--blue) 55%,#1f5fae 100%);overflow:hidden}
.hero-photo{position:absolute;top:0;right:0;width:640px;height:617px;clip-path:polygon(22% 0,100% 0,100% 100%,0 100%);background:linear-gradient(135deg,#dfe7ef 0%,#b9c9d8 40%,#8fa6bd 100%)}
.hero-fade{position:absolute;top:0;left:380px;width:380px;height:617px;background:linear-gradient(90deg,rgba(0,84,170,.9),rgba(0,84,170,0))}
.eyebrow{font-size:12.5px;font-weight:600;letter-spacing:.6px}
.hero .eyebrow{position:absolute;left:96px;top:144px;color:#fff}
.hero h1{position:absolute;left:94px;top:173px;width:560px;font-size:36px;line-height:41px;color:#fff}
.hero p{position:absolute;left:94px;top:310px;width:420px;font-size:13.5px;line-height:20px;color:#eaf2fb}
.btn{position:absolute;height:46px;border-radius:23px;display:flex;align-items:center;justify-content:center;gap:6px;font-size:13px;font-weight:600}
.btn-white{background:#fff;color:var(--blue)}
.btn-ghost{border:2px solid #fff;color:#fff}

/* stats */
.stats{top:692px;height:127px;border-bottom:1px solid #e4e9ef;background:#fff}
.stat{position:absolute;top:22px;width:260px;margin-left:-130px;text-align:center}
.stat-num{font-size:38px;font-weight:700;color:var(--blue);height:52px;line-height:52px}
.stat-ico{height:52px;display:flex;align-items:center;justify-content:center}
.stat-label{font-size:14px;font-weight:600;color:var(--blue);margin-top:6px}

/* section heads */
.sec-mark{width:28px;height:28px;border-radius:50%;border:2px solid var(--blue);margin:0 auto}
.sec-head{position:absolute;left:0;width:1200px;text-align:center}
.sec-head .eyebrow{color:var(--blue);margin-top:8px;font-size:14px}
.sec-head h2{font-size:40px;line-height:44px;margin-top:10px;color:var(--ink)}
.sec-head h2 .hl{color:var(--blue)}

/* services */
.services{top:819px;height:973px}
.card{position:absolute;width:329px;background:#fff;border:1px solid var(--blue-pale);border-radius:6px;box-shadow:0 6px 18px rgba(0,84,170,.08);text-align:center;padding:0 30px}
.card-ico{width:74px;height:70px;margin:32px auto 0;border:1.5px solid var(--blue-pale);border-radius:6px;display:flex;align-items:center;justify-content:center;background:#fff}
.card h3{font-size:18px;font-weight:600;margin-top:26px}
.card p{font-size:12.5px;line-height:19.5px;color:var(--muted);margin-top:10px}
.card.featured{background:linear-gradient(160deg,var(--blue),#0a3f8a);border-color:var(--blue)}
.card.featured h3,.card.featured p{color:#fff}

/* why */
.why{top:1792px;height:904px;background:linear-gradient(180deg,#0d4b9a 0%,var(--blue) 45%,#0b4a96 100%);color:#fff}
.why .sec-mark{border-color:#fff}
.why .sec-head .eyebrow{color:#fff}
.why .sec-head h2{color:#fff;font-size:44px;line-height:46px}
.why-intro{position:absolute;left:150px;top:216px;width:900px;text-align:center;font-size:16.5px;line-height:24px;color:#eef4fb}
.feat{position:absolute;left:604px;width:560px;display:flex;gap:18px}
.feat-ico{width:72px;height:62px;flex:none;background:#fff;border-radius:4px;display:flex;align-items:center;justify-content:center}
.feat h4{font-size:17px;font-weight:600;margin-top:4px}
.feat p{font-size:11px;line-height:17px;color:#dfeaf7;margin-top:4px}

/* process */
.process{top:2696px;height:648px}
.process .sec-head h2{font-size:42px}
.process-sub{position:absolute;left:0;width:1200px;top:202px;text-align:center;font-size:16.5px;color:var(--ink)}
.step{position:absolute;top:232px;width:220px;margin-left:-110px;text-align:center}
.step h4{font-size:17px;font-weight:600;margin-top:12px}
.step p{font-size:11.5px;line-height:17px;color:var(--muted);margin-top:10px}

/* testimonial */
.quote{top:3344px;left:93px;width:1023px;height:339px;background:var(--blue-mist);border-radius:8px}
.quote-mark{position:absolute;left:0;width:1023px;top:66px;text-align:center}
.quote blockquote{position:absolute;left:100px;width:823px;top:112px;text-align:center;font-size:25px;line-height:33px;color:#1b3a6b}
.quote cite{position:absolute;left:0;width:1023px;top:238px;text-align:center;font-style:normal;font-size:16px;font-weight:600;color:var(--blue)}

/* trust */
.trust{top:3730px;height:75px}
.trust-item{position:absolute;top:12px;display:flex;align-items:center;gap:12px;font-size:16px;font-weight:600;color:var(--ink)}
.trust-badge{width:40px;height:40px;border-radius:50%;border:2px solid var(--blue-mid);flex:none}
.sigma{font-family:"Libre Baskerville",serif;font-size:32px;color:var(--blue)}

/* cta */
.cta{top:3805px;height:456px;background:linear-gradient(180deg,#0a3e86,#083877);color:#fff;text-align:center}
.cta .sec-mark{border-color:#fff;margin-top:92px}
.cta .eyebrow{margin-top:14px;font-size:14px}
.cta h2{font-size:52px;line-height:60px;margin-top:8px}
.cta p{font-size:16px;line-height:24px;margin-top:14px;color:#e6eef9}
.cta .btn{top:305px}

/* footer */
.footer{top:4261px;height:344px;background:#fff}
.foot-brand{position:absolute;left:150px;top:52px;display:flex;align-items:center;gap:12px}
.foot-brand .brand-dot{width:52px;height:52px}
.foot-brand .brand-name{font-size:19px}
.foot-about{position:absolute;left:154px;top:134px;width:355px;font-size:13px;line-height:20px;color:var(--ink)}
.foot-col{position:absolute;top:56px}
.foot-col h5{font-size:19px;font-weight:600;letter-spacing:.5px;color:var(--ink)}
.foot-col ul{list-style:none;margin-top:20px}
.foot-col li{font-size:13px;line-height:24px;color:var(--blue)}
.foot-col li::before{content:"» ";color:var(--blue-soft)}
.contact{display:flex;align-items:center;gap:10px;font-size:13px;color:var(--blue);margin-top:12px}
.contact .c{width:24px;height:24px;border-radius:50%;background:var(--blue);flex:none;display:flex;align-items:center;justify-content:center}
.foot-rule{position:absolute;left:93px;width:1034px;top:274px;border-top:1px solid #dde3ea}
.copyright{position:absolute;left:0;width:1200px;top:305px;text-align:center;font-size:12px;color:var(--muted)}
</style>
</head>
<body>

<header class="nav">
  <div class="brand">
    <span class="brand-dot"></span>
    <div><div class="brand-name">Crestline Consulting Group</div><div class="brand-tag">Food Safety &amp; SQF Certification</div></div>
  </div>
  <nav class="nav-links"><span>SERVICES</span><span>BENEFITS</span><span>PROCESS</span><span>CONTACT</span></nav>
  <div class="nav-cta">GET SQF CONSULTATION <span class="arrow-dot"><svg width="12" height="12" viewBox="0 0 12 12"><path d="M3 9 9 3M4 3h5v5" stroke="#0B3F86" stroke-width="1.8" fill="none"/></svg></span></div>
</header>

<section class="hero">
  <div class="hero-photo" role="img" aria-label="Food processing line with workers in white coats and hairnets inspecting products on a conveyor"></div>
  <div class="hero-fade"></div>
  <div class="eyebrow">SQF ONLY · TECH DRIVEN</div>
  <h1 class="serif">Hire a Tech-driven SQF team that carries you across the certification finish line</h1>
  <p>At Crestline Consulting Group, we focus exclusively on SQF — combining real plant experience with smart technology so your team can stay focused on production while we handle the path to certification and beyond.</p>
  <div class="btn btn-white" style="left:91px;top:416px;width:211px">Get SQF Consultation ↗</div>
  <div class="btn btn-ghost" style="left:317px;top:416px;width:203px">Explore Services ↗</div>
</section>

<section class="stats">
  <div class="stat" style="left:173px"><div class="stat-num">15+</div><div class="stat-label">Clients Onboarded</div></div>
  <div class="stat" style="left:429px"><div class="stat-num">100%</div><div class="stat-label">100% SQF Focused</div></div>
  <div class="stat" style="left:708px"><div class="stat-ico"><svg width="52" height="48" viewBox="0 0 52 48" fill="none" stroke="#0054AA" stroke-width="2"><rect x="16" y="14" width="20" height="20" rx="3"/><circle cx="26" cy="24" r="4"/><path d="M26 4v10M26 34v10M6 24h10M36 24h10"/><circle cx="26" cy="4" r="3"/><circle cx="6" cy="24" r="3"/><circle cx="46" cy="24" r="3"/><circle cx="26" cy="44" r="3"/></svg></div><div class="stat-label">Digtial Platform Built Programs</div></div>
  <div class="stat" style="left:1014px"><div class="stat-ico"><svg width="52" height="40" viewBox="0 0 52 40" fill="none" stroke="#0054AA" stroke-width="2"><path d="M4 10h40l4 8-6 12H30l-6 6-8-6H8L4 20z"/><path d="M4 16h20M4 22h20M14 10v20"/></svg></div><div class="stat-label">US Nationwide Coverage</div></div>
</section>

<section class="services">
  <div class="sec-head" style="top:48px">
    <div class="sec-mark"></div>
    <div class="eyebrow">WHAT WE DO</div>
    <h2 class="serif">SQF Consulting, Implementation<br><span class="hl">&amp; Onboarding</span></h2>
  </div>

  <div class="card" style="left:93px;top:241px;height:304px">
    <div class="card-ico"><svg width="36" height="36" viewBox="0 0 36 36" fill="none" stroke="#0054AA" stroke-width="2"><rect x="6" y="4" width="24" height="28" rx="2"/><path d="M11 11h14M11 17h14M11 23h8"/></svg></div>
    <h3>SQF Program Design</h3>
    <p>We design your complete SQF system from scratch — HACCP/food safety plans, prerequisite programs, SOPs, forms, logs, and all required documentation tailored to your facility.</p>
  </div>
  <div class="card featured" style="left:451px;top:236px;height:304px">
    <div class="card-ico" style="background:transparent;border-color:rgba(255,255,255,.6)"><svg width="36" height="36" viewBox="0 0 36 36" fill="none" stroke="#fff" stroke-width="2"><rect x="10" y="10" width="16" height="16" rx="2"/><path d="M14 4v6M22 4v6M14 26v6M22 26v6M4 14h6M4 22h6M26 14h6M26 22h6"/></svg></div>
    <h3>Digital Platform Build</h3>
    <p>We build your SQF program directly into modern food safety software like PlantTrack.io or SafeLedger.io — digitizing forms, checklists, monitoring logs, and workflows so your team runs paperless.</p>
  </div>
  <div class="card" style="left:806px;top:241px;height:304px">
    <div class="card-ico"><svg width="36" height="36" viewBox="0 0 36 36" fill="none" stroke="#0054AA" stroke-width="2"><circle cx="12" cy="12" r="4"/><circle cx="24" cy="12" r="4"/><path d="M4 28c0-5 4-8 8-8s8 3 8 8M16 28c0-5 4-8 8-8s8 3 8 8"/></svg></div>
    <h3>Coaching &amp; Support</h3>
    <p>After building your system, we coach your team to own and maintain it day-to-day. You run the program; we provide ongoing expert guidance so you stay audit-ready at all times.</p>
  </div>
  <div class="card" style="left:93px;top:572px;height:302px">
    <div class="card-ico"><svg width="36" height="36" viewBox="0 0 36 36" fill="none" stroke="#0054AA" stroke-width="2"><path d="M5 28V20M11 28V14M17 28V18"/><circle cx="25" cy="17" r="6"/><path d="M29 21l5 5"/></svg></div>
    <h3>Gap Assessments</h3>
    <p>We evaluate where your facility stands against SQF requirements, identify gaps, and provide a clear roadmap to close them before your audit — no surprises on certification day.</p>
  </div>
  <div class="card" style="left:451px;top:575px;height:302px">
    <div class="card-ico"><svg width="36" height="36" viewBox="0 0 36 36" fill="none" stroke="#0054AA" stroke-width="2"><circle cx="18" cy="11" r="5"/><circle cx="8" cy="15" r="3.5"/><circle cx="28" cy="15" r="3.5"/><path d="M9 30c0-6 4-10 9-10s9 4 9 10"/></svg></div>
    <h3>Bilingual Team Support</h3>
    <p>Our team in Central America supports Spanish-speaking employees within your operation — delivering training, documentation, and coaching in the language your floor team actually speaks.</p>
  </div>
  <div class="card" style="left:806px;top:572px;height:302px">
    <div class="card-ico"><svg width="36" height="36" viewBox="0 0 36 36" fill="none" stroke="#0054AA" stroke-width="2"><rect x="7" y="4" width="20" height="26" rx="2"/><path d="M12 11h10M12 17h10M12 23h5"/><circle cx="26" cy="26" r="6" fill="#0054AA"/><path d="M23 26l2 2 4-4" stroke="#fff"/></svg></div>
    <h3>Sanitation &amp; Regulatory</h3>
    <p>From sanitation program design to environmental monitoring, we help you build internal capabilities that meet USDA, FDA, and FSMA requirements and reduce dependence on external contractors.</p>
  </div>
</section>

<section class="why">
  <div class="sec-head" style="top:54px">
    <div class="sec-mark"></div>
    <div class="eyebrow">WHY CRESTLINE CONSULTING</div>
    <h2 class="serif">Built for Small &amp; Mid-Size<br>Manufacturers</h2>
  </div>
  <p class="why-intro">You don't need to hire a full-time SQF director or figure out SQF alone. We bring the expertise and technology — you stay focused on production.<br>Consultant reviewing digital food safety compliance system in a manufacturing facility.</p>

  <svg class="abs" style="left:9px;top:350px" width="572" height="458" viewBox="0 0 572 458" role="img" aria-label="Consultant reviewing a food safety compliance checklist on a tablet in a manufacturing facility">
    <defs><linearGradient id="hexfill" x1="0" y1="0" x2="1" y2="1"><stop offset="0" stop-color="#e9eef3"/><stop offset=".55" stop-color="#b8c7d6"/><stop offset="1" stop-color="#5f7fa3"/></linearGradient></defs>
    <polygon points="143,4 429,4 568,229 429,454 143,454 4,229" fill="none" stroke="#7BADD7" stroke-width="2"/>
    <polygon points="153,18 419,18 552,229 419,440 153,440 20,229" fill="url(#hexfill)"/>
  </svg>

  <div class="feat" style="top:352px"><div class="feat-ico"><svg width="34" height="34" viewBox="0 0 34 34" fill="none" stroke="#0054AA" stroke-width="2"><circle cx="17" cy="14" r="9"/><path d="M17 9v10M14 11h5a2 2 0 010 4h-4a2 2 0 000 4h5M11 22l-3 9 5-2 4 3M23 22l3 9-5-2"/></svg></div><div><h4>Lower Cost Than a Full-Time Hire</h4><p>Get a complete SQF team — program design, digital implementation, and coaching — at a fraction of the cost of hiring a full-time SQF Practitioner.</p></div></div>
  <div class="feat" style="top:454px"><div class="feat-ico"><svg width="34" height="34" viewBox="0 0 34 34" fill="none" stroke="#0054AA" stroke-width="2"><path d="M17 5 4 12l13 7 13-7zM4 18l13 7 13-7M4 24l13 7 13-7"/></svg></div><div><h4>Your Program Lives in Software</h4><p>No more binders and spreadsheets. Your SQF system is built into PlantTrack.io or SafeLedger.io — organized, accessible, and always audit-ready.</p></div></div>
  <div class="feat" style="top:553px"><div class="feat-ico"><svg width="34" height="34" viewBox="0 0 34 34" fill="none" stroke="#0054AA" stroke-width="2"><circle cx="20" cy="11" r="6"/><path d="M3 22h7l6 3h8a2 2 0 010 4H14M3 29h5l6 2h10l8-6"/></svg></div><div><h4>You Own It, We Support It</h4><p>We build the system and train your team. You maintain and run it day-to-day. We stay on call with coaching and advisory so you never feel stuck.</p></div></div>
  <div class="feat" style="top:649px"><div class="feat-ico"><svg width="34" height="34" viewBox="0 0 34 34" fill="none" stroke="#0054AA" stroke-width="2"><circle cx="17" cy="17" r="7"/><circle cx="17" cy="17" r="2.5"/><path d="M17 4v5M17 25v5M4 17h5M25 17h5M8 8l3 3M23 23l3 3M26 8l-3 3M8 26l3-3"/></svg></div><div><h4>Flexible, Low-Risk Engagement</h4><p>Start with a 3-month commitment, then go month-to-month. Cancel anytime with 30 days notice. We earn your business every month.</p></div></div>
  <div class="feat" style="top:742px"><div class="feat-ico"><svg width="34" height="34" viewBox="0 0 34 34" fill="none" stroke="#0054AA" stroke-width="2"><rect x="3" y="6" width="28" height="18" rx="1"/><path d="M12 30h10M17 24v6"/><circle cx="11" cy="13" r="2.5"/><path d="M7 20c0-3 2-4 4-4s4 1 4 4M19 12h8M19 16h8"/></svg></div><div><h4>Bilingual Floor-Level Support</h4><p>With our Central America team, we provide training and documentation in Spanish so every member of your production team understands and follows the program.</p></div></div>
</section>

<section class="process">
  <div class="sec-head" style="top:34px">
    <div class="sec-mark"></div>
    <div class="eyebrow">HOW IT WORKS</div>
    <h2 class="serif">From Discovery to <span class="hl">Certification</span></h2>
  </div>
  <p class="process-sub">A clear, structured path that takes the guesswork out of SQF.</p>

  <svg class="abs" style="left:0;top:230px" width="1200" height="200" viewBox="0 0 1200 200" fill="none">
    <g>
      <circle cx="234" cy="92" r="84" stroke="#0054AA" stroke-width="4" stroke-dasharray="360 200"/>
      <circle cx="234" cy="92" r="84" stroke="#0054AA" stroke-width="3" stroke-dasharray="2 8" stroke-dashoffset="-360"/>
      <circle cx="234" cy="92" r="64" fill="#0054AA"/>
      <circle cx="234" cy="92" r="46" fill="#fff"/>
      <path d="M218 76c3-3 6-2 8 2l2 5c1 2 0 4-2 5 2 5 6 9 11 11 1-2 3-3 5-2l5 2c4 2 5 5 2 8-3 3-7 4-11 2-10-4-18-12-22-22-2-4-1-8 2-11z" stroke="#0054AA" stroke-width="3"/>
      <circle cx="162" cy="137" r="12" fill="#CADEEF"/><text x="162" y="142" text-anchor="middle" font-family="Poppins,sans-serif" font-size="13" font-weight="600" fill="#0054AA">1</text>
    </g>
    <g>
      <circle cx="474" cy="92" r="84" stroke="#7BADD7" stroke-width="4" stroke-dasharray="360 200"/>
      <circle cx="474" cy="92" r="84" stroke="#0677BA" stroke-width="3" stroke-dasharray="2 8" stroke-dashoffset="-360"/>
      <circle cx="474" cy="92" r="64" fill="#7BADD7"/>
      <circle cx="474" cy="92" r="46" fill="#fff"/>
      <rect x="458" y="72" width="26" height="36" rx="2" stroke="#0054AA" stroke-width="3"/>
      <path d="M464 82h14M464 90h10M464 98h8" stroke="#0054AA" stroke-width="2.5"/>
      <circle cx="486" cy="98" r="7" stroke="#0054AA" stroke-width="3"/><path d="M491 103l6 6" stroke="#0054AA" stroke-width="3"/>
      <circle cx="410" cy="137" r="12" fill="#CADEEF"/><text x="410" y="142" text-anchor="middle" font-family="Poppins,sans-serif" font-size="13" font-weight="600" fill="#0054AA">2</text>
    </g>
    <g>
      <circle cx="706" cy="92" r="84" stroke="#7BADD7" stroke-width="4" stroke-dasharray="360 200"/>
      <circle cx="706" cy="92" r="84" stroke="#0677BA" stroke-width="3" stroke-dasharray="2 8" stroke-dashoffset="-360"/>
      <circle cx="706" cy="92" r="64" fill="#7BADD7"/>
      <circle cx="706" cy="92" r="46" fill="#fff"/>
      <circle cx="706" cy="92" r="14" stroke="#0054AA" stroke-width="3"/><circle cx="706" cy="92" r="5" stroke="#0054AA" stroke-width="3"/>
      <path d="M706 70v8M706 106v8M684 92h8M720 92h8M691 77l5 5M716 102l5 5M721 77l-5 5M691 107l5-5" stroke="#0054AA" stroke-width="3"/>
      <circle cx="654" cy="137" r="12" fill="#CADEEF"/><text x="654" y="142" text-anchor="middle" font-family="Poppins,sans-serif" font-size="13" font-weight="600" fill="#0054AA">3</text>
    </g>
    <g>
      <circle cx="951" cy="92" r="84" stroke="#7BADD7" stroke-width="4" stroke-dasharray="360 200"/>
      <circle cx="951" cy="92" r="84" stroke="#0677BA" stroke-width="3" stroke-dasharray="2 8" stroke-dashoffset="-360"/>
      <circle cx="951" cy="92" r="64" fill="#7BADD7"/>
      <circle cx="951" cy="92" r="46" fill="#fff"/>
      <rect x="935" y="72" width="34" height="24" rx="2" stroke="#0054AA" stroke-width="3"/>
      <circle cx="948" cy="84" r="4" stroke="#0054AA" stroke-width="2.5"/><path d="M956 80h8M956 86h8M930 112h42M940 96l-4 16M962 96l4 16" stroke="#0054AA" stroke-width="2.5"/>
      <circle cx="898" cy="137" r="12" fill="#CADEEF"/><text x="898" y="142" text-anchor="middle" font-family="Poppins,sans-serif" font-size="13" font-weight="600" fill="#0054AA">4</text>
    </g>
  </svg>

  <div class="step" style="left:234px;top:440px"><h4>Discovery Call</h4><p>We learn about your facility, your current systems, and where you are in the SQF journey. No pressure — just a conversation.</p></div>
  <div class="step" style="left:474px;top:438px"><h4>Gap Assessment</h4><p>We evaluate your facility against SQF requirements, identify what's missing, and give you a clear roadmap with priorities.</p></div>
  <div class="step" style="left:706px;top:440px"><h4>Build &amp; Implement</h4><p>We design your SQF program and build it directly into your digital food safety platform — forms, logs, SOPs, HACCP plans, all of it.</p></div>
  <div class="step" style="left:951px;top:440px"><h4>Coach &amp; Certify</h4><p>We train your team, run mock audits, and prepare you for certification day. Then we stay on as your ongoing SQF advisory partner.</p></div>
</section>

<section class="quote">
  <div class="quote-mark"><svg width="56" height="38" viewBox="0 0 56 38"><path d="M2 0h22v20L14 38H4l6-18H2zM32 0h22v20L44 38H34l6-18h-8z" fill="#0054AA"/></svg></div>
  <blockquote class="serif">"Crestline Consulting Group didn't just hand us a binder. They built our entire SQF system into software and coached our team until we owned it. We passed our first audit with confidence."</blockquote>
  <cite>— SQF-Certified Manufacturing Client</cite>
</section>

<section class="trust">
  <div class="trust-item" style="left:140px"><span class="trust-badge"></span>SQF Practitioner</div>
  <div class="trust-item" style="left:390px"><span class="sigma">6σ</span>Six Sigma Black Belt</div>
  <div class="trust-item" style="left:674px"><svg width="42" height="40" viewBox="0 0 42 40" fill="none" stroke="#0677BA" stroke-width="2"><circle cx="21" cy="20" r="7"/><circle cx="21" cy="20" r="2.5"/><circle cx="8" cy="8" r="4"/><circle cx="34" cy="8" r="4"/><circle cx="8" cy="32" r="4"/><circle cx="34" cy="32" r="4"/><path d="M11 11l5 5M31 11l-5 5M11 29l5-5M31 29l-5-5"/></svg>Remote &amp; On-Site</div>
  <div class="trust-item" style="left:944px"><svg width="42" height="40" viewBox="0 0 42 40" fill="none" stroke="#0677BA" stroke-width="2"><rect x="3" y="3" width="36" height="26" rx="2"/><path d="M15 36h12M21 29v7M9 11h10M9 17h10M9 23h6"/><rect x="24" y="10" width="10" height="13"/></svg>Digital-First</div>
</section>

<section class="cta" role="region" aria-label="Call to action over a faint production facility background">
  <div class="sec-mark"></div>
  <div class="eyebrow">GET SQF CONSULTING</div>
  <h2 class="serif">Ready to Talk SQF?</h2>
  <p>Share a few details about your facility and where you are in the SQF journey.<br>We'll follow up with a brief discovery call and a clear next step.</p>
  <div class="btn btn-white" style="left:333px;width:207px;font-size:12.5px">Get My SQF Consultation ↗</div>
  <div class="btn btn-ghost" style="left:605px;width:268px;font-size:12.5px">Visit BatchWise.ai ↗</div>
</section>

<footer class="footer">
  <div class="foot-brand">
    <span class="brand-dot"></span>
    <div><div class="brand-name">Crestline Consulting Group</div><div class="brand-tag">Food Safety &amp; SQF Certification</div></div>
  </div>
  <p class="foot-about">Tech-driven SQF consulting for small and mid-size US food manufacturers. Based in Fresno, CA — serving clients across North America.</p>
  <div class="foot-col" style="left:580px">
    <h5>SERVICES</h5>
    <ul><li>SQF Program Design</li><li>Digital Platform Build</li><li>Coaching &amp; Support</li><li>Gap Assessments</li><li>Sanitation Programs</li></ul>
  </div>
  <div class="foot-col" style="left:836px;top:52px">
    <h5>CONNECT</h5>
    <div class="contact" style="margin-top:16px"><span class="c"><svg width="12" height="10" viewBox="0 0 12 10" fill="none" stroke="#fff" stroke-width="1.4"><rect x="1" y="1" width="10" height="8"/><path d="M1 1l5 4 5-4"/></svg></span>Email Us</div>
    <div class="contact"><span class="c"><svg width="12" height="12" viewBox="0 0 12 12" fill="none" stroke="#fff" stroke-width="1.4"><circle cx="6" cy="6" r="4.5"/><path d="M1.5 6h9M6 1.5c2 2 2 7 0 9M6 1.5c-2 2-2 7 0 9"/></svg></span>BatchWise.ai</div>
    <div class="contact"><span class="c"></span>Professional Network</div>
  </div>
  <div class="foot-rule"></div>
  <div class="copyright">© 2026 Crestline Consulting Group LLC. All rights reserved. Created with Nimbus Studio</div>
</footer>

</body>
</html>
```